Velmora Outcomes Brochure Design Project

- Who we are?
Velmora Outcomes is New Internet Marketing Company Based in China.

It is our aim to provide Chinese clients with the means to internationally market their product, via the Internet.

Our primary products are Outsourced Design ( Thanks to Pixel hive and the amazing designers who use it), SEO and Virtual Hosting.

- Project Brief
Design a vibrant and fresh brochure that introduces the fundamentals of SEO. There is no restriction to the number of pages, however all the info I have included in this brief must be included.

- Colour Palette
Please see link or download the Adobe Swatch Exchange File or follow the link below
http://tintaro.example.com/#themes/search?term=5830716
Updates

Logo updated - grey background removed

Various file formats added for logo and brochure content

Brochure zip file add containing logo in different formats.

Adobe color scheme file added

The general corporate colors are:

Base Color: CMYK :0, 60, 80, 0  Hex: FF6633
Dark Orange: CMYK: 0, 72, 96, 30 Hex: B23308
Light Orange: CMYK 0, 42, 56, 0 Hex: FF9571
Grey: CMYK 0, 0, 0, 48 Hex: 858585
Light Grey: CMYK 0, 0, 0, 26 Hex: BDBDBD

Please note that I'm happy for other colors to be included, however I would like these the corporate branding colors to be clearly present through the brochure.

Hi All

First place payment has increased to $600 - Looking to see some creative designs!

Hi All

Project Deadline Extended
Reason: I have increase the budget and extend the deadline as I need to see more design.

I have attached a zip file that contains example brochures I like.

We are not keen on the table data its a little plain. We have create an info-graphic to replace one of the table and would like to see it included in the design.

Project Deadline Extended
Reason: A few designers have asked for this extension and I would like to see additional designs. Thanks Marek

Target Market(s)

- Our Target Audience is..
It is small to medium businesses looking to reach out to the international market.
Our clients still very much operate on a face to face level in business and are new to the concept of Internet marketing

However this must look professional, Marketable and Clean, with the power of connecting people globally, through SEO and design to be reflected visually in the brochure.

Industry/Entity Type

Internet

Requirements
Must have
• One or more of the FACTS that I have highlighted need to stand out on each page. These FACTS can be found the document attached to this brief and are under the section titled 'Did You Know!'. Not every fact in this section needs to be highlighted in the brochure, but each page needs to have at least, one or more fact that stands out, soemwhere on the page.
See attached document, under the heading 'Did you Know!' and use one or two of these facts to spruce up the pages!

One image/ per page or per two pages MUST be included!

- Provide stock photos and please send us a message with the additional cost of these with your submission

The Table data, that I have included in the attachment must be included in the body of the pages - BUT the table format is not necessary and you can place the information in the body like plain text.

The brochure size should be a little larger than A4.

Please design the back page, like a pocket to hold paper and other material in it that I include with this brochure.

```html
<!DOCTYPE html>
<html lang="en">
<head>
<meta charset="utf-8">
<title>SEO – Velmora Outcomes Brochure Page 6</title>
<link rel="stylesheet" href="https://fonts.googleapis.com/css2?family=Source+Sans+3:wght@400;600&display=swap">
<style>
  :root {
    --orange: #ff6633;
    --brick: #b0372b;
    --heading-red: #b23308;
    --grey: #7d7d7d;
    --ink: #1e1e1e;
    --paper: #ffffff;
  }
  * { margin: 0; padding: 0; box-sizing: border-box; }
  html, body { width: 850px; height: 1200px; overflow: hidden; }
  body {
    font-family: "Source Sans 3", "Myriad Pro", sans-serif;
    color: var(--ink);
    background: var(--paper);
  }
  .page {
    position: relative;
    width: 850px;
    height: 1200px;
    overflow: hidden;
    background:
      radial-gradient(ellipse 700px 260px at 50% 0%, #efefef 0%, rgba(255,255,255,0) 70%),
      radial-gradient(ellipse 700px 260px at 50% 100%, #efefef 0%, rgba(255,255,255,0) 70%),
      var(--paper);
  }
  .frame-marks { position: absolute; inset: 0; pointer-events: none; }

  /* comparison table */
  .compare {
    position: absolute;
    top: 64px;
    background: var(--brick);
    color: #fff;
  }
  .compare--online { left: 95px; width: 338px; }
  .compare--traditional { left: 443px; width: 323px; }
  .compare__head {
    height: 61px;
    display: flex;
    align-items: center;
    font-size: 25px;
    border-bottom: 2px solid #fff;
  }
  .compare--online .compare__head { padding-left: 16px; }
  .compare--traditional .compare__head { justify-content: center; }
  .compare__row { display: flex; border-bottom: 2px solid #fff; }
  .compare__row:last-child { border-bottom: none; }
  .compare__row--first { height: 208px; }
  .compare__row--second { height: 227px; }
  .compare__cell {
    font-size: 15px;
    line-height: 21.5px;
    padding: 8px 0 0 10px;
  }
  .compare__cell + .compare__cell { border-left: 2px solid #fff; }
  .c-label { width: 99px; }
  .c-rating { width: 100px; }
  .c-note { flex: 1; }
  .c-trad { width: 164px; }

  /* packages */
  .packages__title {
    position: absolute;
    left: 96px; top: 604px;
    font-size: 28px;
    font-weight: 400;
    color: var(--heading-red);
  }
  .packages__intro {
    position: absolute;
    left: 96px; top: 645px;
    width: 700px;
    font-size: 15.5px;
    line-height: 29.5px;
  }
  .package-list { list-style: none; }
  .package {
    position: absolute;
    display: flex;
    align-items: center;
    gap: 10px;
    font-size: 15.5px;
  }
  .package svg { width: 40px; height: 36px; flex: none; }

  /* footer */
  .folio {
    position: absolute;
    left: 26px; top: 1137px;
    font-size: 30px;
  }
  .folio-title {
    position: absolute;
    left: 85px; top: 1142px;
    font-size: 21px;
  }
  .fact__label {
    position: absolute;
    left: 383px; top: 1094px;
    width: 447px; height: 24px;
    background: var(--grey);
    color: #fff;
    font-size: 14.5px;
    line-height: 24px;
    padding-left: 8px;
  }
  .fact__body {
    position: absolute;
    left: 300px; top: 1124px;
    width: 520px;
    color: #fff;
    font-size: 14.5px;
    line-height: 19.5px;
    text-align: right;
  }
</style>
</head>
<body>
<main class="page">

  <svg class="frame-marks" width="850" height="1200" viewBox="0 0 850 1200" aria-hidden="true">
    <g stroke="#ff6633" stroke-width="4" fill="none">
      <line x1="92" y1="54" x2="130" y2="54"/>
      <line x1="85" y1="64" x2="85" y2="98"/>
      <line x1="733" y1="54" x2="774" y2="54"/>
      <line x1="781" y1="92" x2="781" y2="120"/>
      <line x1="64" y1="1128" x2="64" y2="1200"/>
      <line x1="68" y1="1176" x2="300" y2="1176"/>
    </g>
    <polygon points="291,1178 340,1118 850,1118 850,1178" fill="#ff6633"/>
  </svg>

  <section class="compare compare--online">
    <div class="compare__head">Online Marketing and SEO</div>
    <div class="compare__row compare__row--first">
      <div class="compare__cell c-label">Ability to<br>target<br>audience</div>
      <div class="compare__cell c-rating">Easy</div>
      <div class="compare__cell c-note">By its very nature,<br>SEO only targets<br>those that are<br>interested in your<br>field or product.<br>The bonus is that<br>your audience is<br>from all over the<br>world</div>
    </div>
    <div class="compare__row compare__row--second">
      <div class="compare__cell c-label">Change<br>marketing<br>based on<br>feedback</div>
      <div class="compare__cell c-rating">Very<br>simple</div>
      <div class="compare__cell c-note">Internet marketing<br>is all about helping<br>you tailoring and<br>automating what<br>the consumer sees,<br>based on feedback,<br>&nbsp;to increase your<br>return on<br>investment</div>
    </div>
  </section>

  <section class="compare compare--traditional">
    <div class="compare__head">Traditional</div>
    <div class="compare__row compare__row--first">
      <div class="compare__cell c-trad">Difficult and costly</div>
      <div class="compare__cell c-note">Traditional media is<br>limited to either a<br>small target audience<br>or a wide<br>non-targeted<br>audience. Internet<br>marketing allows<br>both.</div>
    </div>
    <div class="compare__row compare__row--second">
      <div class="compare__cell c-trad"></div>
      <div class="compare__cell c-note">Traditional marketing<br>takes time to update<br>and distribute, even<br>in the best case<br>scenario you have to<br>update your<br>brochure and get it<br>printed.</div>
    </div>
  </section>

  <h2 class="packages__title">SEO Packages</h2>
  <p class="packages__intro">Whether you are just starting out or are a well-established business, we have an expert package that will suit your needs.<br>All of our packages include the following site optimization activities; this is to make sure that search engines realize you’re the best choice.</p>

  <svg width="0" height="0" style="position:absolute" aria-hidden="true">
    <symbol id="package-icon" viewBox="0 0 40 36">
      <ellipse cx="20" cy="18" rx="19" ry="17" fill="#ff6633"/>
      <ellipse cx="20" cy="18" rx="19" ry="17" fill="none" stroke="#d94a1c" stroke-width="1.5"/>
      <g fill="#fff">
        <rect x="10" y="19" width="4" height="8"/>
        <rect x="15.5" y="14" width="4" height="13"/>
        <rect x="21" y="10" width="4" height="17"/>
        <rect x="26.5" y="16" width="4" height="11"/>
      </g>
    </symbol>
  </svg>

  <ul class="package-list">
    <li class="package" style="left:88px;top:812px"><svg><use href="#package-icon"/></svg>Website Analysis</li>
    <li class="package" style="left:88px;top:871px"><svg><use href="#package-icon"/></svg>Competitive Analysis</li>
    <li class="package" style="left:88px;top:930px"><svg><use href="#package-icon"/></svg>WebSpec Validation</li>
    <li class="package" style="left:88px;top:989px"><svg><use href="#package-icon"/></svg>WebSpec CSS Validation</li>
    <li class="package" style="left:305px;top:812px"><svg><use href="#package-icon"/></svg>Meta Tags Optimization</li>
    <li class="package" style="left:305px;top:871px"><svg><use href="#package-icon"/></svg>Content Optimization</li>
    <li class="package" style="left:305px;top:930px"><svg><use href="#package-icon"/></svg>Image Optimization</li>
    <li class="package" style="left:305px;top:989px"><svg><use href="#package-icon"/></svg>Sitemap Implementation</li>
    <li class="package" style="left:549px;top:812px"><svg><use href="#package-icon"/></svg>Robots.txt Implementation</li>
    <li class="package" style="left:549px;top:871px"><svg><use href="#package-icon"/></svg>Trafficlens Analytics Setup</li>
    <li class="package" style="left:549px;top:930px"><svg><use href="#package-icon"/></svg>Webmasters Tool</li>
  </ul>

  <div class="folio">6</div>
  <div class="folio-title">SEO</div>

  <aside class="fact">
    <div class="fact__label">Did you know that…?</div>
    <p class="fact__body">40% of SEO campaigns aware of their ROI achieve returns in excess of 500%. Companies that blog have 434% more indexed pages. Over 80% of users use search engines to find a website.</p>
  </aside>

</main>
</body>
</html>
```